Dale Porcher Announces his new career move! 8x5 card please.

Associate Broker DALE PORCHER is proud to announce his new affiliation with m.voller sandy cove homes, ltd.

His goal remains to meet all your real estate needs. Prepare to renew your seasonal rental for 2016...with the full support of his new office, Dale can handle your renewal seamlessly.

Prepared to purchase? With access to every property on the market...Dale can show you how easy it making your summer dreams come true can be.

Thinking about selling? m.voller sandy cove homes, ltd. now offers the benefits of the Shared Offering Registry (SOR) to all sellers. In cooperation with SOR Sellers receive the maximum worldwide exposure, Purchasers receive a larger volume of properties to view and in cooperation with other Realtors, the transaction is handled professionally!!!!

I will send logo and photo of Dale Porcher separately. Thank you. M-
Updates

Project Deadline Extended Reason: I would need the cards to be delivered to my office by Friday June 26th for delivery to the public on the 27th. Thank you. Added Wednesday, June 17, 2015

Target Market(s)

Tenants, Sellers & Buyers

Industry/Entity Type

Broker

Font styles to use
Sans Serif

Requirements
Must have
• I attached logo and photo of Dale. Added a better photo of Dale.
Nice to have
• A photo of a property we have listed. I added a couple to choose from.
Should not have
• No Red color

```html
<!DOCTYPE html>
<html lang="en">
<head>
<meta charset="utf-8">
<title>Dale Porcher – Announcement Card</title>
<link href="https://fonts.googleapis.com/css2?family=Lato:ital,wght@0,400;0,700;0,900;1,700&display=swap" rel="stylesheet">
<style>
:root{
  --page:#ffffff;
  --ink:#1c1c1c;
  --orange:#ef9a2a;
  --badge:#2b2b2b;
  --mauve:#9b7a88;
  --teal:#3d97a6;
  --teal-dark:#1f7f7a;
  --stone:#b9b7aa;
  --slate:#7c8f9c;
  --leaf:#97a858;
  --sky:#7ab6d1;
  --sage:#8bb58a;
  --mist:#c9c7c5;
  --ice:#aed6ea;
  --frost:#cfe3ef;
  --sage-light:#c2cfb3;
  --olive:#7e7a34;
  --mint:#8fb08e;
  --sand-1:#e2d3b8;
  --sand-2:#cdb994;
}
*{margin:0;padding:0;box-sizing:border-box}
html,body{width:847px;height:1200px;overflow:hidden;background:var(--page)}
body{position:relative;font-family:'Lato',Arial,sans-serif;color:var(--ink)}
.card{position:absolute;left:33px;width:783px;height:489px;overflow:hidden;background:#fff;box-shadow:0 1px 4px rgba(0,0,0,.25)}
.card--front{top:65px}
.card--back{top:671px}
.tile{position:absolute;width:98px;height:98px}
.photo{position:absolute}
.sand{position:absolute;left:0;top:293px;width:783px;height:196px;
  background:radial-gradient(circle at 30% 40%,var(--sand-1),var(--sand-2) 70%),var(--sand-2)}
.sand-edge{position:absolute;left:0;top:293px;width:783px;height:9px;background:#d6d3cc}
.note{position:absolute;top:331px;width:170px;height:130px;background:rgba(255,255,255,.55)}
.note--left{left:79px;padding:12px 8px;font-weight:700;font-size:12.3px;line-height:15.2px}
.note--left em{font-style:italic}
.note--right{left:534px;padding:22px 0 0 30px;font-weight:700;font-size:12px}
.note--right p{margin-bottom:18px}
.note--right span{color:#666;margin-right:4px}
.badge{position:absolute;left:289px;top:140px;width:200px;height:257px}
.badge-bar{position:absolute;left:263px;top:173px;width:256px;height:42px;background:var(--orange);color:#fff;text-align:center}
.badge-role{font-size:10.5px;letter-spacing:.5px;padding-top:4px;line-height:12px}
.badge-name{font-size:23px;font-weight:900;line-height:24px;letter-spacing:.5px}
.badge-text{position:absolute;left:300px;top:219px;width:178px;text-align:center;color:#fff;font-style:italic;font-weight:700;font-size:10px;line-height:13px}
.portrait{position:absolute;left:337px;top:260px;width:104px;height:125px;background:linear-gradient(180deg,#3a3a3a,#5a4a40 60%,#222)}
.cta{position:absolute;left:487px;top:98px;width:296px;height:98px;background:var(--orange);color:#fff;font-weight:700;font-size:16.5px;display:flex;align-items:center;justify-content:center}
.copy{position:absolute;left:82px;top:214px;width:620px;font-size:13px;line-height:16.5px}
.copy h2{color:var(--orange);font-size:13px;font-weight:900;line-height:16px}
.copy p{margin-bottom:16px}
.contact{position:absolute;left:82px;top:385px;font-weight:700;font-size:11.5px;line-height:19px}
.contact-rule{width:110px;height:3px;background:var(--orange);margin-bottom:6px}
.contact span{color:#666;margin-right:4px}
.brand{position:absolute;right:86px;top:378px;display:flex;align-items:center;gap:8px;font-weight:700;font-size:13px;color:#1b6b3f}
.brand-mark{width:12px;height:12px;background:#1b6b3f}
</style>
</head>
<body>

<section class="card card--front">
  <div class="photo" role="img" aria-label="Boardwalk through trees" style="left:0;top:0;width:98px;height:98px;background:linear-gradient(160deg,#a9b7a4,#6d7a5a)"></div>
  <div class="photo" role="img" aria-label="Modern house lit at dusk by a pool" style="left:98px;top:0;width:98px;height:98px;background:linear-gradient(180deg,#8a6a58,#c79a6a 50%,#4f6f8a)"></div>
  <div class="tile" style="left:196px;top:0;background:var(--mauve)"></div>
  <div class="photo" role="img" aria-label="Deck facing the ocean" style="left:293px;top:0;width:98px;height:98px;background:linear-gradient(180deg,#9fb6c8,#6d8190 50%,#5a5a50)"></div>
  <div class="photo" role="img" aria-label="Ceiling fan in a wood room" style="left:391px;top:0;width:98px;height:98px;background:linear-gradient(160deg,#c6a783,#8c6b4c)"></div>
  <div class="tile" style="left:489px;top:0;background:var(--teal)"></div>
  <div class="photo" role="img" aria-label="Garden patio with umbrella" style="left:586px;top:0;width:98px;height:98px;background:linear-gradient(160deg,#c9d3d8,#6c8a52)"></div>
  <div class="photo" role="img" aria-label="Wooden gate under blue sky" style="left:684px;top:0;width:99px;height:98px;background:linear-gradient(180deg,#7aa9d6,#6a5440)"></div>

  <div class="tile" style="left:0;top:98px;background:var(--stone)"></div>
  <div class="tile" style="left:98px;top:98px;background:var(--teal-dark)"></div>
  <div class="photo" role="img" aria-label="Swimming pool" style="left:196px;top:98px;width:98px;height:98px;background:linear-gradient(180deg,#8a8578,#4aa6d8 40%,#2f86c4)"></div>
  <div class="tile" style="left:293px;top:98px;background:var(--slate)"></div>
  <div class="photo" role="img" aria-label="House exterior" style="left:391px;top:98px;width:98px;height:98px;background:linear-gradient(180deg,#a0b0b8,#6a6d68)"></div>
  <div class="photo" role="img" aria-label="White patio umbrellas on a deck" style="left:489px;top:98px;width:98px;height:98px;background:linear-gradient(160deg,#e8e4dc,#5a5a58)"></div>
  <div class="tile" style="left:586px;top:98px;background:var(--leaf)"></div>
  <div class="tile" style="left:684px;top:98px;width:99px;background:var(--sky)"></div>

  <div class="tile" style="left:0;top:196px;background:var(--sage)"></div>
  <div class="photo" role="img" aria-label="Bright living room interior" style="left:98px;top:196px;width:98px;height:98px;background:linear-gradient(160deg,#e6e8e6,#9aa09a)"></div>
  <div class="tile" style="left:196px;top:196px;background:var(--mist)"></div>
  <div class="tile" style="left:293px;top:196px;width:196px;background:var(--slate)"></div>
  <div class="tile" style="left:489px;top:196px;background:var(--ice)"></div>
  <div class="photo" role="img" aria-label="Living room with ocean view" style="left:586px;top:196px;width:98px;height:98px;background:linear-gradient(180deg,#b99a72,#6d8da0 50%,#8c6a3e)"></div>
  <div class="tile" style="left:684px;top:196px;width:99px;background:var(--frost)"></div>

  <div class="sand" role="img" aria-label="Sand texture"></div>
  <div class="sand-edge"></div>

  <div class="note note--left">His goal remains to meet all your real estate needs. Prepare to <em>renew</em> your seasonal rental for 2016... with the full support of his new office, Dale can handle your renewal seamlessly.</div>
  <div class="note note--right">
    <p>sandycovehomes.com</p>
    <p><span>Ph</span>555.201.4400</p>
    <p><span>C</span>&nbsp; 555.318.6622</p>
  </div>

  <svg class="badge" viewBox="0 0 200 257" aria-hidden="true">
    <path d="M16 0H184A16 16 0 0 0 200 16V241A16 16 0 0 0 184 257H16A16 16 0 0 0 0 241V16A16 16 0 0 0 16 0Z" fill="#2b2b2b"/>
    <path d="M19 5H181A19 19 0 0 0 195 19V238A19 19 0 0 0 181 252H19A19 19 0 0 0 5 238V19A19 19 0 0 0 19 5Z" fill="none" stroke="#fff" stroke-width="1.5"/>
  </svg>
  <div class="badge-bar">
    <div class="badge-role">ASSOCIATE BROKER</div>
    <div class="badge-name">DALE PORCHER</div>
  </div>
  <p class="badge-text">is proud to announce his new affiliation with m.voller sandy cove homes, ltd.</p>
  <div class="portrait" role="img" aria-label="Portrait of Dale Porcher"></div>
</section>

<section class="card card--back">
  <div class="photo" role="img" aria-label="Outdoor dining table at sunset" style="left:0;top:0;width:98px;height:98px;background:linear-gradient(180deg,#9aa4ae,#6e6a50 60%,#8a7656)"></div>
  <div class="photo" role="img" aria-label="White kitchen with bar stools" style="left:98px;top:0;width:98px;height:98px;background:linear-gradient(160deg,#eeeeec,#8e8e88)"></div>
  <div class="tile" style="left:196px;top:0;background:var(--mint)"></div>
  <div class="photo" role="img" aria-label="Deck chairs overlooking the bay" style="left:293px;top:0;width:196px;height:196px;background:linear-gradient(180deg,#4e8fd0,#9cc4e4 40%,#6a9ab4 55%,#8f8a80)"></div>
  <div class="tile" style="left:489px;top:0;background:var(--ice)"></div>
  <div class="photo" role="img" aria-label="Living room with white sofas" style="left:586px;top:0;width:98px;height:98px;background:linear-gradient(160deg,#5a4a3c,#e8ecef 60%,#6a8fb8)"></div>
  <div class="photo" role="img" aria-label="Garden dining set under umbrella" style="left:684px;top:0;width:99px;height:98px;background:linear-gradient(180deg,#e6e2d8,#5f8a48 50%,#9a7a52)"></div>

  <div class="tile" style="left:0;top:98px;background:var(--sage-light)"></div>
  <div class="tile" style="left:98px;top:98px;background:var(--olive)"></div>
  <div class="photo" role="img" aria-label="Deck with cushions" style="left:196px;top:98px;width:98px;height:98px;background:linear-gradient(160deg,#8a6a4c,#b0744e 60%,#6a5440)"></div>
  <div class="cta">Contact Dale Porcher today!</div>

  <div class="copy">
    <h2>Prepared to purchase?</h2>
    <p>With access to every property on the market...Dale can show you how easy it making your summer dreams come true can be.</p>
    <h2>Thinking about selling?</h2>
    <p>m.voller sandy cove homes, ltd. now offers the benefits of the Shared Offering Registry (SOR) to all sellers. In cooperation with SOR Sellers receive the maximum worldwide exposure, Purchasers receive a larger volume of properties to view and in cooperation with other Realtors, the transaction is handled professionally!!!!</p>
  </div>

  <div class="contact">
    <div class="contact-rule"></div>
    sandycovehomes.com<br>
    <span>Ph</span>555.201.4400<br>
    <span>C</span>&nbsp; 555.318.6622
  </div>

  <div class="brand"><span class="brand-mark"></span>m.voller sandy cove homes, ltd.</div>
</section>

</body>
</html>
```